Church Lanterns Over Millbrook Gospel Booklet Design

We need a booklet designed that we will be printing to hand out in our community. Wording for each page will be provided and we need graphic design to produce the layouts in a format ready for print. Booklet will be 4.75" x 4.75" square and a total of 12 pages: 1 cover page front, 1 cover page back, 10 inside pages some of which will be full spread across 2 pages.

Target Market(s)

English speaking Westerners

Industry/Entity Type

Religious

Font styles to use
Serif

Colors
ffffff
85abd2
0292cd
33b8a4
5c5c5c

Requirements
Must have
• Minimalist design with clean look described in attached document
Nice to have
• Aesthetically pleasing graphics, crisp fonts, excellent turn around times
Should not have
• Effeminate design, busy look with too much graphic and text

```html
<!DOCTYPE html>
<html lang="en">
<head>
<meta charset="utf-8">
<title>Lanterns Over Millbrook – Booklet Layout</title>
<link rel="stylesheet" href="https://fonts.googleapis.com/css2?family=Noto+Serif:ital,wght@0,400;0,700;1,400&family=Open+Sans:wght@400&display=swap">
<style>
:root{
  --white:#ffffff;
  --sky:#85abd2;
  --blue:#0292cd;
  --teal:#33b8a4;
  --ink:#5c5c5c;
  --board:#a6a6a6;
  --text:#333333;
}
*{margin:0;padding:0;box-sizing:border-box}
html,body{width:1200px;height:1076px;overflow:hidden;background:var(--board)}
body{position:relative;font-family:"Noto Serif",Georgia,serif;color:var(--text)}
.label{position:absolute;width:280px;text-align:center;font-family:"Open Sans",Arial,sans-serif;font-size:15px;color:#333}
.spread{position:absolute;width:560px;height:280px;display:flex;box-shadow:0 7px 8px rgba(0,0,0,.45)}
.page{position:relative;width:280px;height:280px;background:var(--white);overflow:hidden}
.page.verso::after{content:"";position:absolute;right:0;top:0;width:22px;height:100%;background:linear-gradient(to left,rgba(0,0,0,.08),transparent)}
.page.recto::before{content:"";position:absolute;left:0;top:0;width:22px;height:100%;background:linear-gradient(to right,rgba(0,0,0,.1),transparent);z-index:2}
.abs{position:absolute}
.body{position:absolute;font-size:6.2px;line-height:1.55;color:var(--text)}
.body p+p{margin-top:6px}
.ref{position:absolute;height:9px;background:var(--blue);color:var(--white);font-size:6px;font-weight:700;line-height:9px;padding-left:38px}
.quote{position:absolute;font-style:italic;font-size:11.5px;line-height:1.38;color:var(--ink)}
.block-teal{position:absolute;background:var(--teal)}
.block-sky{position:absolute;background:var(--sky)}
.photo{position:absolute}
.foot{position:absolute;left:28px;top:264px;width:224px;display:flex;align-items:center;gap:4px;font-size:5.4px;color:var(--ink);letter-spacing:.2px;white-space:nowrap}
.foot i{flex:1;height:1px;background:var(--sky)}
.foot i.t{background:var(--teal)}
.tab{position:absolute;left:106px;top:274px;width:67px;height:6px;background:var(--blue)}
.wordmark{position:absolute;color:var(--blue);font-weight:700;line-height:1.05}
.truths{position:absolute;left:28px;top:82px;width:246px}
.truth{display:flex;gap:4px;height:31px}
.truth .key{display:flex;gap:1px;height:7px;width:43px;flex:none}
.truth .key b{width:5px}
.truth .key span{flex:1;color:#fff;font-size:5.5px;line-height:7px;text-align:right;padding-right:3px;font-style:italic}
.truth p{font-size:6.2px;line-height:1.5;font-style:italic;border-bottom:1px solid #aaa;width:170px;height:24px}
.steps{position:absolute;left:27px;top:45px;width:220px;font-size:6.2px;line-height:1.55}
.steps h2{font-size:6.6px;font-weight:400;letter-spacing:.2px;margin-bottom:10px}
.steps ul{margin-top:5px;padding-left:11px}
.steps li{margin-bottom:5px}
.banner{position:absolute;left:27px;top:190px;height:17px;display:flex;gap:2px}
.banner b{width:4px}
.banner span{background:var(--teal);color:#fff;font-size:12px;font-style:italic;line-height:17px;padding:0 5px}
.verse{position:absolute;left:0;top:44px;width:280px;text-align:center;font-style:italic;text-transform:uppercase;color:var(--white);font-size:14.5px;line-height:1.45}
.verse .hi{color:var(--teal);font-size:16.5px}
.verse-ref{position:absolute;left:0;top:220px;width:280px;display:flex;justify-content:center;align-items:center;gap:5px;color:#fff;font-size:6px;font-weight:700}
.verse-ref i{width:20px;height:1px;background:#fff}
</style>
</head>
<body>

<div class="label" style="left:22px;top:36px">Back</div>
<div class="label" style="left:325px;top:36px">Front</div>
<div class="label" style="left:603px;top:36px">Page 2</div>
<div class="label" style="left:903px;top:36px">Page 3</div>
<div class="label" style="left:20px;top:362px">Page 4</div>
<div class="label" style="left:321px;top:362px">Page 5</div>
<div class="label" style="left:612px;top:362px">Page 6</div>
<div class="label" style="left:912px;top:362px">Page 7</div>
<div class="label" style="left:17px;top:700px">Page 8</div>
<div class="label" style="left:318px;top:700px">Page 9</div>
<div class="label" style="left:612px;top:700px">Page 10</div>
<div class="label" style="left:913px;top:700px">Page 11</div>

<!-- Covers -->
<div class="spread" style="left:30px;top:64px">
  <div class="page cover-back">
    <div class="photo" role="img" aria-label="Forested mountain ridges under a golden sunset sky" style="left:0;top:0;width:252px;height:188px;background:linear-gradient(to bottom,#b9b3c4 0%,#e2b17b 30%,#f2a552 38%,#7c8a6a 52%,#3f5a2f 75%,#2c4323 100%)"></div>
    <div class="abs" style="left:0;top:188px;width:252px;height:4px;background:var(--ink)"></div>
    <div class="wordmark" style="left:64px;top:24px;font-size:16px;width:170px">Lanterns Over Millbrook</div>
    <div class="block-sky" style="left:252px;top:0;width:28px;height:280px"></div>
  </div>
  <div class="page cover-front">
    <div class="block-sky" style="left:0;top:0;width:28px;height:280px;background:#7aa2cf"></div>
    <div class="photo" role="img" aria-label="Mountain valley with river and wildflowers at sunset" style="left:28px;top:0;width:252px;height:280px;background:linear-gradient(to bottom,#c9b5a4 0%,#eeb27a 18%,#f19a4a 30%,#9f7d66 42%,#6f7a53 58%,#435c2a 78%,#2f4620 100%)"></div>
    <div class="wordmark" style="left:70px;top:34px;font-size:24px;width:200px">Lanterns Over Millbrook</div>
  </div>
</div>

<!-- Pages 2–3 -->
<div class="spread" style="left:608px;top:64px">
  <div class="page verso">
    <div class="photo" role="img" aria-label="Silhouette with raised arms against a bright sky and clouds" style="left:0;top:0;width:280px;height:280px;background:radial-gradient(ellipse at 50% 25%,#ffffff 0%,#b9d6ef 18%,#4f7fb4 45%,#1b2d4a 75%,#06080c 100%)"></div>
    <div class="foot" style="color:#ccc"><i></i>LANTERNS OVER MILLBROOK<i class="t"></i></div>
    <div class="tab"></div>
  </div>
  <div class="page recto">
    <div class="body" style="left:28px;top:48px;width:180px"><p>God willingly created the universe, meaning he envisioned, designed, and made us.</p></div>
    <div class="ref" style="left:28px;top:88px;width:87px">GENESIS 1:1</div>
    <div class="quote" style="left:67px;top:102px;width:200px">“In the beginning God created the heavens and the earth.”</div>
    <div class="block-teal" style="left:28px;top:158px;width:93px;height:60px"></div>
    <div class="photo" role="img" aria-label="Spiral galaxy in deep space" style="left:128px;top:158px;width:124px;height:60px;background:radial-gradient(ellipse at 55% 45%,#e9d8e6 0%,#8b6e9a 22%,#2d2a45 55%,#0b0b14 100%)"></div>
    <div class="block-sky" style="left:260px;top:158px;width:20px;height:60px"></div>
    <div class="foot"><i class="t"></i>LANTERNS OVER MILLBROOK<i></i></div>
    <div class="tab"></div>
  </div>
</div>

<!-- Pages 4–5 -->
<div class="spread" style="left:30px;top:390px">
  <div class="page verso">
    <div class="body" style="left:28px;top:46px;width:150px"><p>This reality establishes some foundational truths for all of us:</p></div>
    <div class="truths">
      <div class="truth"><div class="key"><b style="background:#d6e3f1"></b><b style="background:#b4cbe4"></b><span style="background:var(--sky)">1.</span></div><p>God loves us - he didn’t have to create us; we are here because he couldn’t imagine life without us.</p></div>
      <div class="truth"><div class="key"><b style="background:#9fd3ec"></b><b style="background:#55b5df"></b><span style="background:var(--blue)">2.</span></div><p>God is the proper authority in our lives - if he designed and made us, he rightfully owns us.</p></div>
      <div class="truth"><div class="key"><b style="background:#bfe6df"></b><b style="background:#85d2c5"></b><span style="background:var(--teal)">3.</span></div><p>God knows the purpose of our lives - if he designed and made us, he knows why we are here.</p></div>
      <div class="truth"><div class="key"><b style="background:#bdbdbd"></b><b style="background:#8c8c8c"></b><span style="background:var(--ink)">4.</span></div><p style="border:none">God’s truth is the truth we need - if he designed and made us, he knows what it takes for life to go well for us.</p></div>
    </div>
    <div class="foot"><i></i>LANTERNS OVER MILLBROOK<i class="t"></i></div>
    <div class="tab"></div>
  </div>
  <div class="page recto">
    <div class="body" style="left:28px;top:46px;width:172px"><p>But we, mankind, have all rejected God’s authority in our lives. And because he rightfully owns us, our rebellion against God is a grave injustice; an act of treason for which we deserve to be cut off from God forever.</p></div>
    <div class="ref" style="left:28px;top:115px;width:92px">ROMANS 6:23</div>
    <div class="quote" style="left:68px;top:130px;width:200px">“For the wages of sin is death...”</div>
    <div class="block-teal" style="left:28px;top:163px;width:93px;height:61px"></div>
    <div class="photo" role="img" aria-label="Cemetery with gravestones under trees" style="left:128px;top:163px;width:124px;height:61px;background:linear-gradient(to bottom,#8fae6a 0%,#5b7a3c 40%,#4a4f4c 70%,#6d6b62 100%)"></div>
    <div class="block-sky" style="left:260px;top:163px;width:20px;height:61px"></div>
    <div class="foot"><i class="t"></i>LANTERNS OVER MILLBROOK<i></i></div>
    <div class="tab"></div>
  </div>
</div>

<!-- Pages 6–7 -->
<div class="spread" style="left:608px;top:390px">
  <div class="page verso">
    <div class="block-sky" style="left:0;top:149px;width:20px;height:60px"></div>
    <div class="body" style="left:27px;top:46px;width:190px">
      <p>This alienation from God is evident in a myriad of ways including poverty, crime, conflict in our relationships, and our internal struggles.</p>
      <p>But worse, when we die, we must face the consequences for our rejection of God by spending eternity in hell - a lake of fire created by God as the place where our treason is brought to justice.</p>
    </div>
    <div class="photo" role="img" aria-label="Roaring orange flames" style="left:27px;top:149px;width:125px;height:60px;background:radial-gradient(ellipse at 50% 55%,#ff8a2a 0%,#d9401a 40%,#6e1508 75%,#220603 100%)"></div>
    <div class="block-teal" style="left:158px;top:149px;width:94px;height:60px"></div>
    <div class="foot"><i></i>LANTERNS OVER MILLBROOK<i class="t"></i></div>
    <div class="tab"></div>
  </div>
  <div class="page recto">
    <div class="body" style="left:28px;top:46px;width:190px">
      <p>But God does not want you to pay for your own sins. God loves us so much he sent his only son to save us.</p>
      <p>Jesus Christ died on the cross to serve our sentence for our rebellion against God and rose again on the third day. Since Christ paid our full penalty, we can be completely forgiven and reconciled to God.</p>
    </div>
    <div class="ref" style="left:28px;top:133px;width:81px">JOHN 3:16</div>
    <div class="quote" style="left:67px;top:147px;width:205px">“For God so loved the world that he sent his one and only son that whosoever believes in him will not perish but have eternal life.”</div>
    <div class="foot"><i class="t"></i>LANTERNS OVER MILLBROOK<i></i></div>
    <div class="tab"></div>
  </div>
</div>

<!-- Pages 8–9 -->
<div class="spread" style="left:30px;top:729px">
  <div class="page verso">
    <div class="steps">
      <h2>HERE IS WHAT YOU MUST DO TO BE SAVED:</h2>
      <p>First, ask Jesus Christ to save you (Since he is God, he can hear you):</p>
      <ul>
        <li>Acknowledge that God is the rightful authority of the universe and your life.</li>
        <li>Apologize to him for your rebellion against God.</li>
        <li>Ask Jesus Christ to come into your life as your Lord and Savior.</li>
        <li>This decision will immediately trigger his miracle of salvation in you.</li>
      </ul>
    </div>
    <div class="banner"><b style="background:#c8ebe4"></b><b style="background:#8fd7ca"></b><span>GOD NOW LIVES IN YOU!</span></div>
    <div class="foot"><i></i>LANTERNS OVER MILLBROOK<i class="t"></i></div>
    <div class="tab"></div>
  </div>
  <div class="page recto">
    <div class="block-teal" style="left:28px;top:47px;width:93px;height:60px"></div>
    <div class="photo" role="img" aria-label="Wooden cross silhouetted against a fiery red sunset" style="left:128px;top:47px;width:124px;height:60px;background:radial-gradient(ellipse at 50% 60%,#ffd36a 0%,#f07a22 30%,#b3261a 65%,#3d0a08 100%)"></div>
    <div class="block-sky" style="left:260px;top:47px;width:20px;height:60px"></div>
    <div class="ref" style="left:28px;top:124px;width:92px">ROMANS 10:9</div>
    <div class="quote" style="left:68px;top:138px;width:205px">“If you confess with your mouth that Jesus is Lord and believe in your heart that God raised him from the dead, you will be saved.”</div>
    <div class="foot"><i class="t"></i>LANTERNS OVER MILLBROOK<i></i></div>
    <div class="tab"></div>
  </div>
</div>

<!-- Pages 10–11 -->
<div class="spread" style="left:608px;top:729px">
  <div class="page verso">
    <div class="body" style="left:27px;top:46px;width:172px">
      <p>Next, God has given us the Bible and his church as the key tools for us to grow in our understanding of God and our personal relationship with him.</p>
      <p>So, it is essential you find a local church that believes the Bible is 100% true. Tell one of the pastors you are a brand new Christian and they will help you from there.</p>
    </div>
    <div class="block-sky" style="left:0;top:149px;width:20px;height:60px"></div>
    <div class="photo" role="img" aria-label="Folded hands resting on an open Bible" style="left:27px;top:149px;width:125px;height:60px;background:linear-gradient(to bottom,#eef1f4 0%,#d9dde2 50%,#c9b89a 80%,#e9e2d2 100%)"></div>
    <div class="block-teal" style="left:158px;top:149px;width:94px;height:60px"></div>
    <div class="foot"><i></i>LANTERNS OVER MILLBROOK<i class="t"></i></div>
    <div class="tab"></div>
  </div>
  <div class="page recto">
    <div class="photo" role="img" aria-label="Lone tree on a misty mountain under a deep blue night sky" style="left:0;top:0;width:280px;height:280px;background:linear-gradient(to bottom,#22407e 0%,#2c4b85 35%,#4a5d78 60%,#2c3a4c 80%,#141c26 100%)"></div>
    <div class="verse">
      <div class="hi">“FOR OUR SAKE</div>
      <div>HE MADE HIM TO BE SIN</div>
      <div>WHO KNEW NO SIN,</div>
      <div class="hi">SO THAT IN HIM</div>
      <div>WE MIGHT BECOME</div>
      <div class="hi">THE RIGHTEOUSNESS</div>
      <div class="hi">OF GOD.”</div>
    </div>
    <div class="verse-ref"><i></i>2 CORINTHIANS 5:21<i></i></div>
    <div class="foot" style="color:#9fb0c8"><i class="t"></i>LANTERNS OVER MILLBROOK<i></i></div>
    <div class="tab"></div>
  </div>
</div>

</body>
</html>
```